'Tarvel' a financial/crypto-currency exchange in the middle east

On the card we need 1) Name 2) title 3) email address 4) phone number using the same colors and theme as the logo. On one side we just want the logo and we want the whole card to be in blue (same blue as logo) with the logo in the back being white.
Industry/Entity Type
Financial

```html
<!DOCTYPE html>
<html lang="en">
<head>
<meta charset="UTF-8">
<title>Tarvel – Business Card</title>
<link href="https://fonts.googleapis.com/css2?family=Montserrat:wght@400;600;700&display=swap" rel="stylesheet">
<style>
  :root {
    --backdrop: #1f93d3;
    --card-blue: #2495d2;
    --card-blue-light: #3aa3db;
    --white: #ffffff;
  }
  * { margin: 0; padding: 0; box-sizing: border-box; }
  html, body {
    width: 1200px;
    height: 943px;
    overflow: hidden;
  }
  body {
    background: var(--backdrop);
    font-family: "Montserrat", Arial, sans-serif;
    color: var(--white);
    position: relative;
  }
  .card {
    position: absolute;
    top: 279px;
    width: 387px;
    height: 386px;
    background: linear-gradient(200deg, var(--card-blue-light) 0%, var(--card-blue) 60%, #1c8ecd 100%);
    box-shadow: 0 2px 4px rgba(0, 40, 80, 0.35);
    overflow: hidden;
  }
  .card--front { left: 187px; }
  .card--back  { left: 625px; }

  .corner-disc {
    position: absolute;
    left: 234px;
    top: 11px;
    width: 148px;
    height: 148px;
    border-radius: 50%;
    background: var(--white);
  }
  .contact {
    position: absolute;
    left: 37px;
    top: 212px;
  }
  .contact__name {
    font-weight: 700;
    font-size: 29px;
    letter-spacing: 0.3px;
    line-height: 1.1;
  }
  .contact__title {
    font-weight: 400;
    font-size: 19px;
    margin-top: 2px;
  }
  .contact__rule {
    width: 36px;
    height: 4px;
    background: var(--white);
    margin: 16px 0 14px;
  }
  .contact__line {
    font-weight: 400;
    font-size: 19px;
    line-height: 28px;
    letter-spacing: 0.2px;
  }

  .brand {
    position: absolute;
    left: 49px;
    top: 150px;
    display: flex;
    align-items: center;
    gap: 16px;
  }
  .brand__dot {
    width: 86px;
    height: 86px;
    border-radius: 50%;
    background: var(--white);
  }
  .brand__name {
    font-weight: 700;
    font-size: 46px;
    letter-spacing: 0.5px;
  }
</style>
</head>
<body>
  <section class="card card--front" aria-label="Business card front">
    <div class="corner-disc"></div>
    <div class="contact">
      <p class="contact__name">Karim Nassar</p>
      <p class="contact__title">Founder &amp; CEO</p>
      <div class="contact__rule"></div>
      <p class="contact__line">555.210.4836</p>
      <p class="contact__line">karim@tarvel.com</p>
    </div>
  </section>

  <section class="card card--back" aria-label="Business card back">
    <div class="brand">
      <div class="brand__dot"></div>
      <span class="brand__name">Tarvel</span>
    </div>
  </section>
</body>
</html>
```